Pals of Rusty Fundraiser Flyer for shelter dogs

Flyer for Fund Raiser for shelter and rescue dogsThis will be hosted by who we are calling Heroes First responders (Fire, Police, and EMS will be bartending raising money to help the shelter dogs).

I will be uploading a basic flyer I did but I don't like it, only showing for dates and words etc...

struggling to come up with something eye-catching related to the above.

We can keep the use of Heroes (spelled wrong on the flyer)but open for new ideas too and new title.

Target Market(s)

Animal lovers

Font styles to use
Serif
Sans Serif

Requirements
Must have
• the ties to first responders and dog rescue
• Must include First responder logo badges images. The image with the helping hands Maybe replace the badges with images of dogs or doggy paws something like that
• Must have a strong presence identifying and relating to first responders
• Images of first responders as well as even images of the first responder logos for fire department police department and EMS.
• The first responders are the ones hosting the event so we really want to raise them up and show their appreciation for the cause that is super important as well
• Title should read
• Guardians Guarding Mutts

```html
<!DOCTYPE html>
<html lang="en">
<head>
<meta charset="utf-8">
<title>Guardians Guarding Mutts – Pals of Rusty</title>
<link href="https://fonts.googleapis.com/css2?family=Anton&family=Montserrat:wght@300;700;800;900&family=Open+Sans:ital,wght@0,400;0,600;1,400;1,700&display=swap" rel="stylesheet">
<style>
  :root {
    --red: #e30d0d;
    --deep-red: #b90808;
    --black: #0b0b0b;
    --white: #ffffff;
    --paper: #f7f7f7;
    --stage: #e6e6e6;
    --ink: #111111;
  }
  * { box-sizing: border-box; margin: 0; padding: 0; }
  html, body { width: 1200px; height: 1200px; overflow: hidden; background: var(--stage); }
  .flyer {
    position: absolute; left: 194px; top: 20px;
    width: 812px; height: 1160px;
    background: var(--paper); overflow: hidden;
    font-family: "Montserrat", sans-serif;
  }
  .flyer svg.art { position: absolute; left: 0; top: 0; }
  .date {
    position: absolute; left: 62px; top: 124px;
    color: var(--white); font-weight: 800; font-size: 34px; line-height: 40px; letter-spacing: 0.5px;
  }
  .title { position: absolute; left: 40px; top: 170px; color: var(--ink); }
  .title .rule { width: 350px; height: 3px; background: var(--ink); }
  .title .big {
    font-family: "Anton", sans-serif; font-size: 100px; line-height: 108px;
    letter-spacing: -1px; text-transform: uppercase;
  }
  .title .mid {
    font-weight: 300; font-size: 50px; line-height: 54px; color: var(--white);
    display: flex; align-items: center; gap: 10px;
  }
  .title .mid .stars { color: var(--ink); font-size: 34px; letter-spacing: 2px; }
  .title .bottom {
    font-weight: 900; font-size: 76px; line-height: 86px; text-transform: uppercase;
    letter-spacing: -1px;
  }
  .title .rule.under { width: 350px; height: 2px; margin-top: 4px; }
  .brand {
    position: absolute; right: 34px; top: 38px; width: 220px; text-align: center;
  }
  .brand .dot { width: 96px; height: 96px; border-radius: 50%; background: var(--red); margin: 0 auto 12px; }
  .brand .name { font-weight: 700; font-size: 24px; color: var(--ink); }
  .brand .sub { font-weight: 700; font-size: 11px; color: var(--ink); letter-spacing: 0.3px; margin-top: 2px; }
  .time {
    position: absolute; right: 30px; top: 830px; text-align: right; color: var(--white);
  }
  .time .hours { font-weight: 800; font-size: 58px; line-height: 62px; }
  .time .host { font-family: "Open Sans", sans-serif; font-weight: 600; font-size: 19px; line-height: 24px; }
  .time .venue { font-weight: 800; font-size: 25px; line-height: 32px; }
  .responders {
    position: absolute; left: 32px; top: 988px; display: flex; gap: 22px;
  }
  .badge {
    width: 96px; height: 96px; border-radius: 50%; background: var(--red);
    border: 3px solid var(--deep-red);
    display: flex; align-items: flex-end; justify-content: center; padding-bottom: 18px;
    color: var(--white); font-weight: 800; font-size: 17px;
  }
  .pitch {
    position: absolute; left: 400px; top: 978px; width: 390px;
    border-left: 3px solid var(--red); padding-left: 12px;
    font-family: "Open Sans", sans-serif; font-style: italic; color: var(--white);
    font-size: 16px; line-height: 22px;
  }
  .pitch .lead { color: var(--red); font-weight: 700; font-size: 18px; margin-bottom: 2px; }
  .contacts {
    position: absolute; left: 30px; right: 30px; top: 1112px;
    display: flex; justify-content: space-between; align-items: center;
    font-family: "Open Sans", sans-serif; font-weight: 600; font-size: 17px; color: var(--ink);
  }
  .contacts span { display: flex; align-items: center; gap: 7px; }
  .contacts i { width: 13px; height: 13px; border-radius: 50%; background: var(--red); display: inline-block; }
</style>
</head>
<body>
<main class="flyer">
  <svg class="art" width="812" height="1160" viewBox="0 0 812 1160">
    <polygon class="red-band" points="157,0 534,0 0,1010 0,232" fill="var(--red)"/>
    <rect role="img" aria-label="Photo of a smiling beagle with a collar" x="440" y="290" width="372" height="670" fill="url(#hound)"/>
    <circle role="img" aria-label="Photo of a police officer shaking paws with a dark shepherd dog" cx="354" cy="580" r="100" fill="url(#officer)" stroke="var(--red)" stroke-width="5"/>
    <circle role="img" aria-label="Photo of a volunteer kneeling beside a shepherd dog" cx="287" cy="790" r="135" fill="url(#volunteer)" stroke="var(--red)" stroke-width="5"/>
    <polygon class="time-box" points="515,818 812,818 812,958 440,958" fill="var(--red)"/>
    <rect class="info-band" x="0" y="965" width="812" height="130" fill="var(--black)"/>
    <defs>
      <radialGradient id="hound" cx="0.55" cy="0.4" r="0.6">
        <stop offset="0" stop-color="#c98a4e"/><stop offset="0.6" stop-color="#e9dccd"/><stop offset="1" stop-color="#f7f7f7"/>
      </radialGradient>
      <linearGradient id="officer" x1="0" y1="0" x2="0" y2="1">
        <stop offset="0" stop-color="#7c9a5e"/><stop offset="1" stop-color="#4a4f5a"/>
      </linearGradient>
      <linearGradient id="volunteer" x1="0" y1="0" x2="0" y2="1">
        <stop offset="0" stop-color="#c9d6dc"/><stop offset="0.5" stop-color="#7a7f5a"/><stop offset="1" stop-color="#7c7c80"/>
      </linearGradient>
    </defs>
  </svg>

  <div class="date">AUG 15, 2019</div>
  <h1 class="title">
    <div class="rule"></div>
    <div class="big">Guardians</div>
    <div class="mid">GUARDING <span class="stars">★★★</span></div>
    <div class="bottom">Mutts</div>
    <div class="rule under"></div>
  </h1>

  <div class="brand">
    <div class="dot"></div>
    <div class="name">Pals of Rusty</div>
    <div class="sub">MAPLE COUNTY DOG SHELTER</div>
  </div>

  <div class="time">
    <div class="hours">6-10PM</div>
    <div class="host">Hosted at</div>
    <div class="venue">THE HARBOR ROOM</div>
  </div>

  <div class="responders">
    <div class="badge">FIRE</div>
    <div class="badge">POLICE</div>
    <div class="badge">EMS</div>
  </div>

  <p class="pitch">
    <span class="lead">Join Pals of Rusty for an evening of fun!</span><br>
    Come spend an evening with our Celebrity Bartenders and help some pups in need our local men and women in uniform will be pouring drinks and raising awareness for adoption.
  </p>

  <div class="contacts">
    <span><i></i>@PalsOfRustyMCDS</span>
    <span><i></i>www.palsofrustymaple.org</span>
    <span><i></i>@porscds</span>
  </div>
</main>
</body>
</html>
```